Lotus Market Hall VIP Card(Magnetic strip plastic card)

We need Fancy,Simple,VIP customer card design for a grocery store name"Lotus Market Hall", Chinese name"鸿福商场“.Major color should be Dark red. This design is based on a VIP gift card project, which means design should consider about the back side with magnetic strip area and mostly it will be plastic material.

Target Market(s)

Rich Customers

Industry/Entity Type

Grocery Store

Contact Information for Business Card

People actually put more than $1000 into the card for shopping

Font styles to use
Serif
Sans Serif
Decorative
Script
Other font styles liked:
• Fancy

Colors
ec1f27
fbed22

Requirements
Must have
• Red color
Nice to have
• Better logo transformation.

```html
<!DOCTYPE html>
<html lang="en">
<head>
<meta charset="utf-8">
<title>Lotus Market Hall VIP Card</title>
<link href="https://fonts.googleapis.com/css2?family=Didact+Gothic&family=Noto+Sans+SC:wght@300&display=swap" rel="stylesheet">
<style>
  :root {
    --page: #ffffff;
    --red-deep: #b8152a;
    --red-bright: #ec1f27;
    --gold: #fbed22;
    --white: #ffffff;
    --stripe: #3a3739;
    --silver: #e6e6e6;
    --silver-edge: #cfcfcf;
    --ink-soft: #5a5a5a;
    --rule: #2b2b2b;
  }
  html, body {
    margin: 0;
    padding: 0;
    overflow: hidden;
    background: var(--page);
  }
  .sheet {
    position: relative;
    width: 1200px;
    height: 736px;
    background: var(--page);
    overflow: hidden;
  }
  .card {
    position: absolute;
    width: 511px;
    height: 270px;
  }
  .card--front-a { left: 76px; top: 70px; }
  .card--back-a  { left: 615px; top: 70px; }
  .card--front-b { left: 76px; top: 371px; }
  .card--back-b  { left: 615px; top: 371px; }
  .brand-cn {
    font-family: "Noto Sans SC", sans-serif;
    font-weight: 300;
    font-size: 90px;
    fill: var(--white);
  }
  .brand-en {
    font-family: "Didact Gothic", sans-serif;
    font-size: 34px;
  }
  .brand-en--gold { fill: var(--gold); }
  .brand-en--white { fill: var(--white); }
  .holder {
    font-family: "Didact Gothic", sans-serif;
    font-size: 22px;
    fill: var(--white);
  }
  .initials {
    font-family: "Didact Gothic", sans-serif;
    font-size: 34px;
  }
  .initials--light { fill: var(--white); }
  .initials--dark { fill: var(--ink-soft); }
  .base-rule {
    position: absolute;
    left: 0;
    top: 679px;
    width: 1200px;
    height: 2px;
    background: var(--rule);
  }
</style>
</head>
<body>
<main class="sheet">

  <!-- Front, deep red variant -->
  <svg class="card card--front-a" viewBox="0 0 511 270" aria-label="Lotus Market Hall VIP card front">
    <defs><clipPath id="clipA"><rect width="511" height="270" rx="14"/></clipPath></defs>
    <g clip-path="url(#clipA)">
      <rect width="511" height="270" fill="var(--red-deep)"/>
      <polygon points="8,0 511,0 511,152 160,152" fill="var(--red-bright)"/>
    </g>
    <text class="brand-cn" x="77" y="150" textLength="357" lengthAdjust="spacingAndGlyphs">鸿福商场</text>
    <text class="brand-en brand-en--gold" x="79" y="195" textLength="354" lengthAdjust="spacingAndGlyphs">LOTUS MARKET HALL</text>
  </svg>

  <!-- Back, red variant -->
  <svg class="card card--back-a" viewBox="0 0 511 270" aria-label="Lotus Market Hall VIP card back">
    <defs><clipPath id="clipB"><rect width="511" height="270" rx="14"/></clipPath></defs>
    <g clip-path="url(#clipB)">
      <rect width="511" height="270" fill="var(--red-bright)"/>
      <polygon points="0,0 502,0 350,152 0,152" fill="var(--red-deep)"/>
      <rect class="mag-stripe" y="197" width="511" height="42" fill="var(--stripe)"/>
    </g>
    <text class="holder" x="19" y="41">Firstname Lastname</text>
    <text class="holder" x="19" y="70">Card ID</text>
    <text class="initials initials--light" x="500" y="186" text-anchor="end">LMH</text>
  </svg>

  <!-- Front, bright red variant -->
  <svg class="card card--front-b" viewBox="0 0 511 270" aria-label="Lotus Market Hall VIP card front, bright variant">
    <defs><clipPath id="clipC"><rect width="511" height="270" rx="14"/></clipPath></defs>
    <g clip-path="url(#clipC)">
      <rect width="511" height="270" fill="var(--red-bright)"/>
      <polygon points="8,0 511,0 511,153 160,153" fill="var(--red-deep)"/>
    </g>
    <text class="brand-cn" x="77" y="151" textLength="357" lengthAdjust="spacingAndGlyphs">鸿福商场</text>
    <text class="brand-en brand-en--white" x="79" y="196" textLength="354" lengthAdjust="spacingAndGlyphs">LOTUS MARKET HALL</text>
  </svg>

  <!-- Back, silver variant -->
  <svg class="card card--back-b" viewBox="0 0 511 270" aria-label="Lotus Market Hall VIP card back, silver variant">
    <defs><clipPath id="clipD"><rect width="511" height="270" rx="14"/></clipPath></defs>
    <g clip-path="url(#clipD)">
      <rect width="511" height="270" fill="var(--silver)"/>
      <polygon points="0,0 502,0 350,153 0,153" fill="var(--red-deep)"/>
      <rect class="mag-stripe" y="197" width="511" height="42" fill="var(--stripe)"/>
    </g>
    <rect x="0.5" y="0.5" width="510" height="269" rx="14" fill="none" stroke="var(--silver-edge)"/>
    <text class="holder" x="19" y="42">Firstname Lastname</text>
    <text class="holder" x="19" y="71">Card ID</text>
    <text class="initials initials--dark" x="500" y="187" text-anchor="end">LMH</text>
  </svg>

  <div class="base-rule"></div>
</main>
</body>
</html>
```